The Marlowfield Career mentor

The service is premium. It is aimed at people 18-30, so students and those looking to change their first job, principally in the UK but also global. It is offering a very personalised CV writing service and is much more expensive than others on offer. I am very keen that it should look simple and premium. It needs to look very professional, reflecting the aspirational jobs that the clients will be applying for.
If there were three words that summed it up: modern, clean, premium.
I am waiting for all the testimonials to come in but they need to form a major part of the website.
I am also waiting for the full logo design files so that I can upload them. In the meantime there is a copy of the logo.
Thoughts to help those yet to send a design...
This is a premium service and some of the designs have looked very generic. The focus needs to be on quality and the process mentioned in the brief. The partnership and the advantages it brings are crucial but few have mentioned that.

```html
<!DOCTYPE html>
<html lang="en">
<head>
<meta charset="utf-8">
<title>The Marlowfield Career Mentor</title>
<link href="https://fonts.googleapis.com/css2?family=Cormorant+Garamond:wght@500;600;700&family=Lato:wght@400;700&display=swap" rel="stylesheet">
<style>
:root{
  --blue:#1468b3;
  --blue-dark:#0f5aa0;
  --ink:#222;
  --muted:#333;
  --white:#fff;
  --footer:#000;
  --star:#f5a623;
  --line:#9aa4ae;
  --grey-band:#6f6f6f;
}
*{box-sizing:border-box;margin:0;padding:0}
html,body{width:1200px;height:3454px;overflow:hidden}
body{font-family:'Lato',sans-serif;color:var(--ink);background:var(--white);position:relative}
.wrap{position:absolute;left:110px;right:110px}

/* header */
.topbar{position:absolute;top:0;left:0;width:1200px;height:110px}
.brand{position:absolute;left:110px;top:34px;font-family:'Cormorant Garamond',serif;font-weight:600;color:var(--blue);font-size:30px;letter-spacing:1px;text-transform:uppercase;line-height:1}
.brand small{display:block;font-size:18px;letter-spacing:3px;margin-top:6px}
.mail{position:absolute;left:718px;top:34px;display:flex;gap:12px;align-items:center;white-space:nowrap}
.mail .lbl{font-family:'Cormorant Garamond',serif;color:var(--blue);font-size:15px}
.mail .val{font-family:'Cormorant Garamond',serif;font-size:16px;font-weight:600;color:#111}
.btn{display:inline-block;background:var(--blue);color:var(--white);font-family:'Cormorant Garamond',serif;font-weight:700;font-size:18px;letter-spacing:.5px;border-radius:24px 0 24px 24px;text-transform:uppercase}
.btn-head{position:absolute;left:934px;top:35px;width:153px;height:42px;line-height:42px;text-align:center;background:linear-gradient(90deg,#2c6ca8,#1468b3)}

.nav{position:absolute;top:110px;left:0;width:1200px;height:56px;background:var(--blue)}
.nav ul{list-style:none;position:absolute;left:110px;top:0;display:flex;height:56px;align-items:center}
.nav li{font-family:'Cormorant Garamond',serif;color:var(--white);font-weight:700;font-size:16px;letter-spacing:.5px;text-transform:uppercase}
.call{position:absolute;left:903px;top:0;width:297px;height:56px;background:var(--grey-band);display:flex;align-items:center;gap:12px;padding-left:12px;color:var(--white)}
.call .ic{width:38px;height:38px;border-radius:50%;background:var(--white);display:flex;align-items:center;justify-content:center}
.call .lbl{font-size:11px;font-weight:700}
.call .num{font-size:18px;font-weight:700}

/* hero */
.hero{position:absolute;top:166px;left:0;width:1200px;height:509px;background:linear-gradient(90deg,#6a6b6e 0%,#8a8a8c 30%,#c9c2b8 55%,#a07a5e 70%,#d9d6d2 85%,#3e3a3a 100%)}
.hero-text{position:absolute;left:110px;top:112px;color:var(--white);font-family:'Cormorant Garamond',serif;text-transform:uppercase;font-weight:600}
.hero-text .a{font-size:32px;letter-spacing:2px}
.hero-text .b{font-size:48px;letter-spacing:2px;margin-top:22px}
.hero-text .c{font-size:32px;letter-spacing:2px;margin-top:20px}
.btn-hero{position:absolute;left:110px;top:317px;width:170px;height:47px;line-height:47px;text-align:center;background:var(--white);color:var(--blue);font-size:17px}

/* intro */
.questions{top:738px;font-size:17px;line-height:58px}
.acc{position:absolute;left:110px;width:980px;height:59px;border:1px solid var(--line);border-radius:6px;padding:0 25px;line-height:57px;font-size:17px;white-space:nowrap}
.para{position:absolute;left:134px;width:950px;font-size:15.5px;line-height:29px}

/* partnership */
.partner-bg{position:absolute;top:1620px;left:0;width:1200px;height:571px;background:linear-gradient(180deg,#fff 0%,#f0f0f0 100%)}
.h2{position:absolute;left:0;width:1200px;text-align:center;font-family:'Cormorant Garamond',serif;font-weight:700;font-size:44px;color:var(--blue)}
.partner-img{position:absolute;left:111px;top:1765px;width:411px;height:355px;border-radius:6px;background:linear-gradient(135deg,#6d7480,#c9cdd3 45%,#e8e6e4 70%,#5b6475)}
.partner-copy{position:absolute;left:597px;top:1758px;width:490px;font-size:15px;line-height:29px}
.btn-partner{position:absolute;left:601px;top:2070px;width:171px;height:47px;line-height:47px;text-align:center}

/* testimonials */
.testi{position:absolute;top:2191px;left:0;width:1200px;height:842px;background:var(--blue);overflow:hidden}
.testi .h2{top:58px;color:var(--white)}
.card{position:absolute;width:329px;background:var(--white);border-radius:10px;padding:22px 24px;font-size:13px;line-height:26px;color:#222}
.card .q{font-family:'Cormorant Garamond',serif;font-weight:700;font-size:80px;line-height:60px;color:#888;height:40px;overflow:hidden}
.card .meta{display:flex;justify-content:space-between;align-items:flex-end;margin-top:14px;font-size:15px;line-height:25px}
.stars{color:var(--star);letter-spacing:4px;font-size:15px}
.row1{top:142px;height:255px}
.row2{top:430px;height:209px;overflow:hidden;background:linear-gradient(180deg,#fff 0%,#dbe7f3 45%,#4d8ccb 100%)}
.row2 p{color:#4a78a8}
.fade{position:absolute;left:0;top:560px;width:1200px;height:90px;background:linear-gradient(180deg,rgba(20,104,179,0),var(--blue))}
.btn-more{position:absolute;left:528px;top:2915px;width:145px;height:42px;line-height:42px;text-align:center;background:var(--white);color:var(--blue);font-size:17px}

/* footer */
.footer{position:absolute;top:3033px;left:0;width:1200px;height:421px;background:var(--footer);color:var(--white)}
.fbrand{position:absolute;left:110px;top:68px;font-family:'Cormorant Garamond',serif;font-weight:600;font-size:26px;letter-spacing:1px;text-transform:uppercase;line-height:1}
.fbrand small{display:block;font-size:15px;letter-spacing:3px;margin-top:5px}
.social{position:absolute;left:110px;top:163px;display:flex;gap:26px}
.social span{width:32px;height:32px;border-radius:50%;background:var(--white)}
.fcol{position:absolute;top:98px}
.fcol h4{font-family:'Cormorant Garamond',serif;font-weight:700;font-size:21px;margin-bottom:14px}
.fcol h4.light{font-weight:500}
.fcol ul{list-style:none;font-size:15px;line-height:34px}
.fcol li::before{content:"➜";margin-right:10px;font-size:13px}
.contact-row{display:flex;gap:12px;align-items:center;font-size:15px;line-height:26px;margin-bottom:18px;white-space:nowrap}
.contact-row .ic{width:32px;height:32px;border-radius:50%;background:var(--white);flex:none;display:flex;align-items:center;justify-content:center}
.frule{position:absolute;left:110px;top:338px;width:980px;height:1px;background:#555}
.copy{position:absolute;left:0;top:376px;width:1200px;text-align:center;font-family:'Cormorant Garamond',serif;font-size:16px}
</style>
</head>
<body>

<header class="topbar">
  <div class="brand">Marlowfield<small>Career Mentor</small></div>
  <div class="mail">
    <svg width="34" height="34" viewBox="0 0 34 34" fill="none" stroke="#1468b3" stroke-width="1.6"><rect x="3" y="12" width="28" height="18" rx="1"/><path d="M3 12l14 10 14-10M8 12V4h18v8"/><circle cx="17" cy="9" r="2.5"/></svg>
    <div><div class="lbl">Send Us Email</div><div class="val">hello@mcm-mentor.com</div></div>
  </div>
  <div class="btn btn-head">Contact Us</div>
</header>

<nav class="nav">
  <ul>
    <li style="width:130px">Home</li>
    <li style="width:168px">About Us</li>
    <li style="width:160px">Services</li>
    <li style="width:204px">Testimonials</li>
    <li>Latest News</li>
  </ul>
  <div class="call">
    <div class="ic"><svg width="20" height="20" viewBox="0 0 24 24" fill="none" stroke="#555" stroke-width="1.8"><path d="M5 3h4l2 5-3 2a12 12 0 0 0 6 6l2-3 5 2v4a2 2 0 0 1-2 2A17 17 0 0 1 3 5a2 2 0 0 1 2-2z"/></svg></div>
    <div><div class="lbl">Call Us</div><div class="num">+1 555 014 2290</div></div>
  </div>
</nav>

<section class="hero" role="img" aria-label="Photograph of a smiling professional in a tan blazer at a desk with a laptop, meeting a client">
  <div class="hero-text">
    <div class="a">Welcome to</div>
    <div class="b">The Marlowfield</div>
    <div class="c">Career Mentor</div>
  </div>
  <div class="btn btn-hero">Get Started</div>
</section>

<div class="wrap questions">
  <p>Is your current CV not getting you results?</p>
  <p>Do you want to create a CV that stands out from the crowd?</p>
  <p>Do you want to get a job more quickly?</p>
  <p>Do you want to earn more for the job your searching for?</p>
</div>

<div class="acc" style="top:987px">If so then invest in a CV writing partnership with Adrian, the Marlowfield career mentor.?</div>
<p class="para" style="top:1061px">But first read the testimonials. These are real results from real people. They invested in the partnership approach, and they’re delighted because it works. The blurb that follows is not as important as what they say – I’d &nbsp;love it if you were the next person to appear in these testimonials. .</p>

<div class="acc" style="top:1175px">People I work with get a job sooner and get a higher paid job..?</div>
<div class="para" style="top:1250px">
  <p>Working with me is personalised, it’s a partnership. Together we will build a great CV that will present you in the best way possible, it will increase the chances of you securing the job you want. And you’ll also get this. As a result of my approach everyone I’ve worked with is better prepared for interview. Our partnership will</p>
  <p style="margin-top:29px">·Increase self awareness<br>·Improve presentation skills<br>·Build the right sort of confidence</p>
  <p style="margin-top:29px">And as a result you’ll impress at interview. You’ll develop a language and way of expressing yourself that shows the very best of you. And as that language sinks in and becomes part of you, you project a genuine confidence, quietly powerful, that recruiters will want in their teams.</p>
</div>

<div class="partner-bg"></div>
<h2 class="h2" style="top:1670px">The Partnership</h2>
<div class="partner-img" role="img" aria-label="Photograph of three business people in suits gathered around a meeting table reviewing documents"></div>
<div class="partner-copy">
  <p>The key to all this success is the partnership. Over four sessions we will, together, build a CV. You will get me, no one else, working with you for four sessions. There is a formula for success but it’s not formulaic. Your CV will be personal, you will shine through. Your CV will be elevated above the crowd.</p>
  <p style="margin-top:29px">I offer a premium service, very different to other offerings - so if like those in the testimonials, you get that job sooner, get a higher paid job, the investment is a wise one.So take the first step to the best CV you can have. Contact me now.</p>
</div>
<div class="btn btn-partner">Contact Us</div>

<section class="testi">
  <h2 class="h2">What Customer Says</h2>

  <div class="card row1" style="left:-39px">
    <div class="q">“</div>
    <p>Temporibus autem quibusdam et aut officiis debitis aut rerum necessitatibus saepe eveniet ut et voluptates repudiandae sint et molestiae non recusandae. expensive ones that another</p>
    <div class="meta"><div>Maren<br>Excellent Work</div><div class="stars">★★★★★</div></div>
  </div>
  <div class="card row1" style="left:322px">
    <div class="q">“</div>
    <p>Itaque earum rerum hic tenetur a sapiente delectus, ut aut reiciendis voluptatibus maiores alias consequatur aut perferendis doloribus asperiores repellat</p>
    <div class="meta"><div>Maren<br>Excellent Work</div><div class="stars">★★★★★</div></div>
  </div>
  <div class="card row1" style="left:683px">
    <div class="q">“</div>
    <p>Temporibus autem quibusdam et aut officiis debitis aut rerum necessitatibus saepe eveniet ut et voluptates repudiandae sint et molestiae non recusandae. correct filters.</p>
    <div class="meta"><div>Delia F<br>Life Savers</div><div class="stars">★★★★★</div></div>
  </div>
  <div class="card row1" style="left:1042px">
    <div class="q">“</div>
    <p>Temporibus autem quibusdam et aut officiis debitis aut rerum necessitatibus saepe ut et voluptates repudiandae non recusandae. ng done</p>
    <div class="meta"><div>Delia F<br>Life Savers</div></div>
  </div>

  <div class="card row2" style="left:-184px">
    <div class="q">“</div>
    <p>They did a great job with our HVAC equipment. They were professional, and responsive. I</p>
  </div>
  <div class="card row2" style="left:173px">
    <div class="q">“</div>
    <p>Temporibus autem quibusdam et aut officiis debitis aut rerum necessitatibus saepe eveniet ut et voluptates repudiandae sint et molestiae non recusandae.</p>
    <p>Maren</p>
  </div>
  <div class="card row2" style="left:534px">
    <div class="q">“</div>
    <p>Temporibus autem quibusdam et aut officiis debitis aut rerum necessitatibus saepe eveniet ut et voluptates repudiandae sint et molestiae non recusandae.</p>
    <p>Maren</p>
  </div>
  <div class="card row2" style="left:892px">
    <div class="q">“</div>
    <p>Itaque earum rerum hic tenetur a sapiente delectus, ut aut reiciendis voluptatibus maiores alias consequatur aut perferendis doloribus asperiores repellat</p>
    <p>Maren</p>
  </div>
  <div class="fade"></div>
</section>
<div class="btn btn-more">View More</div>

<footer class="footer">
  <div class="fbrand">Marlowfield<small>Career Mentor</small></div>
  <div class="social" aria-label="Social links"><span></span><span></span><span></span><span></span></div>

  <div class="fcol" style="left:429px">
    <h4>Quick Links</h4>
    <ul><li>Home</li><li>About</li><li>Services</li><li>Testimonials</li><li>Contact Us</li></ul>
  </div>
  <div class="fcol" style="left:661px">
    <h4 class="light">Help Links</h4>
    <ul><li>FAQ</li><li>Terms of use</li><li>Privacy Policy</li><li>Support Links</li><li>Conditions</li></ul>
  </div>
  <div class="fcol" style="left:897px">
    <h4>Contact Us</h4>
    <div class="contact-row"><div class="ic"><svg width="14" height="18" viewBox="0 0 14 18"><path d="M7 0a7 7 0 0 1 7 7c0 5-7 11-7 11S0 12 0 7a7 7 0 0 1 7-7z" fill="#000"/><circle cx="7" cy="7" r="2.5" fill="#fff"/></svg></div><div>MCM<br>United States</div></div>
    <div class="contact-row"><div class="ic"><svg width="16" height="16" viewBox="0 0 24 24" fill="none" stroke="#000" stroke-width="2"><path d="M5 3h4l2 5-3 2a12 12 0 0 0 6 6l2-3 5 2v4a2 2 0 0 1-2 2A17 17 0 0 1 3 5a2 2 0 0 1 2-2z"/></svg></div><div>+1 555 014 2290</div></div>
    <div class="contact-row"><div class="ic"><svg width="16" height="12" viewBox="0 0 16 12"><rect width="16" height="12" rx="1.5" fill="#000"/><path d="M1 1l7 5 7-5" stroke="#fff" stroke-width="1.4" fill="none"/></svg></div><div>hello@mcm-mentor.com</div></div>
  </div>

  <div class="frule"></div>
  <div class="copy">Copyrights@2024.MCM.All Rights Reserved</div>
</footer>

</body>
</html>
```